Kleine Werbebroschüre für Bauunternehmen (Deckblatt plus  1. und 2. Seite)
Kleine Werbebroschüre für Bauunternehmen (Deckblatt plus 1. und 2. Seite)
Zielgruppe
Private Bauherren, Familien
Aufgabenstellung
Guten Tag zusammen,
wir benötigen einen klein Broschüre für ein Bauunternehmen, welche angelehnt werden kann an das Design unserer Internetseite www.kolbe-steinbau.de. Die Broschüre soll nur aus einem Deckblatt und dann beim Aufklappen aus einer ersten und zweiten Seite bestehen, die Rückseite kann frei bleiben bzw. hier genügt ein kleiner farblicher Balken mit z. B. unseren Kontaktinformationen. Die Bilder, Logos und Texte, welche verarbeitet werden sollen, laden wir gerne über das Portal hoch. Zur ganz groben Orientierung haben wir ein Word Dokument angelegt und hochgeladen, das Hausbild auf dem Deckblatt muss nicht, aber kann eingebaut werden, es muss sich halt gut in das Gesamtbild einfügen. Wir wünschen uns eine modernes, hochwertiges und vertrauenserweckendes Design, die Website soll nur zur Orientierung gelten und Eure Kreativität nicht einschränken. Wir sind für alle Vorschläge offen. Wenn es fragen gibt, sind wir jederzeit für Euch ansprechbar.
Wir freuen uns auf Eure Vorschläge.
Jörg

```html
<!DOCTYPE html>
<html lang="de">
<head>
<meta charset="utf-8">
<title>Kolbe Steinbau – Leistungen</title>
<link href="https://fonts.googleapis.com/css2?family=Ubuntu:wght@400;500&display=swap" rel="stylesheet">
<style>
  :root {
    --ink: #2a2c30;
    --accent: #4a5a7c;
    --accent-dark: #3d4a66;
    --paper: #f3f4f2;
    --link: #3a4f80;
  }
  * { margin: 0; padding: 0; box-sizing: border-box; }
  html, body { width: 848px; height: 1200px; overflow: hidden; }
  body {
    font-family: "Ubuntu", sans-serif;
    color: var(--ink);
    background: radial-gradient(ellipse at 60% 40%, #fbfbfa 0%, var(--paper) 60%, #e9eaea 100%);
    position: relative;
  }
  .section-head {
    position: absolute; left: 22px; width: 781px;
    border-bottom: 2px solid var(--accent);
    height: 40px;
  }
  .section-head h2 {
    position: absolute; left: 24px; bottom: 2px;
    font-weight: 400; font-size: 23.5px; color: var(--accent); letter-spacing: 0.5px;
  }
  .section-head .icons { position: absolute; right: 0; bottom: 3px; display: flex; gap: 26px; }
  .section-head svg { width: 40px; height: 36px; display: block; }
  .copy {
    position: absolute; left: 35px; width: 750px;
    font-size: 11px; line-height: 13.7px; letter-spacing: 0.25px;
  }
  .copy p + p { margin-top: 13.7px; }
  .copy a { color: var(--link); text-decoration: none; font-weight: 500; }
  .models { position: absolute; top: 464px; left: 22px; display: flex; gap: 5px; }
  .model {
    position: relative; width: 192px; height: 81px;
    border: 1px solid var(--accent);
    background: linear-gradient(180deg, #6f8fc0 0%, #9ab4d6 35%, #6e8a4a 70%, #4f6a34 100%);
  }
  .model .tag {
    position: absolute; right: 0; bottom: 0; width: 84px; height: 15px;
    background: rgba(240,241,243,0.85); color: var(--accent);
    font-size: 11.5px; text-align: center; line-height: 15px; letter-spacing: 0.5px;
  }
  .specs { position: absolute; top: 699px; left: 36px; list-style: none; font-size: 11.5px; letter-spacing: 0.3px; }
  .specs li { height: 20.5px; display: flex; align-items: center; }
  .specs li::before {
    content: ""; width: 9px; height: 9px; border-radius: 2px; margin-right: 7px; flex: none;
    background: var(--accent-dark); box-shadow: inset 0 0 0 1px #27304a;
  }
  .site-url {
    position: absolute; right: 29px; top: 1165px;
    font-size: 15.5px; color: var(--accent); letter-spacing: 0.4px;
  }
</style>
</head>
<body>

<header class="section-head" style="top:18px">
  <h2>Schall- und Brandschutzverhalten</h2>
  <div class="icons">
    <svg viewBox="0 0 40 36" fill="none" stroke="#4a5a7c" stroke-width="3"><path d="M3 17 L20 4 L37 17"/><path d="M7 14 V33 H33 V14"/><path d="M15 20 h3 l4 -4 v12 l-4 -4 h-3z" fill="#4a5a7c" stroke-width="1"/><path d="M25 19 q2 3 0 6" stroke-width="1.6"/></svg>
    <svg viewBox="0 0 40 36" fill="none" stroke="#4a5a7c" stroke-width="3"><path d="M3 17 L20 4 L37 17"/><path d="M7 14 V33 H33 V14"/><path d="M20 14 c4 4 7 7 7 11 a7 6 0 0 1 -14 0 c0 -3 2 -5 3 -6 c0 3 2 4 3 4 c-1 -3 0 -6 1 -9z" fill="#4a5a7c" stroke="none"/></svg>
  </div>
</header>
<div class="copy" style="top:77px; left:34px">
  <p>Aufgrund der höheren Dichte der Baustoffe, schützt ein Massivhaus seine Bewohner wesentlich besser vor äußerer, ständig zunehmender Lärmeinwirkung aus der Umwelt.</p>
  <p>Durch die mineralischen, nicht brennbaren Baustoffe wird eine Brandverbreitung wesentlich vermindert. Zudem entstehen keine giftigen Rauchgase.</p>
  <p>Wasserschäden, wie sie durch jede Waschmaschine oder durch Löschen eines Brandes entstehen können, haben im Massivhaus aufgrund der diffusionsoffenen Eigenschaften der Bauteile nur kleine Auswirkungen und trocknen leicht wieder aus, ohne bleibende Schäden zu hinterlassen.</p>
</div>

<header class="section-head" style="top:234px">
  <h2>Baukosten</h2>
  <div class="icons">
    <svg viewBox="0 0 40 36" fill="none" stroke="#4a5a7c" stroke-width="3"><path d="M3 17 L20 4 L37 17"/><path d="M7 14 V33 H33 V14"/><text x="20" y="29" font-size="15" font-family="Ubuntu, sans-serif" font-weight="500" fill="#4a5a7c" stroke="none" text-anchor="middle">€</text></svg>
  </div>
</header>
<div class="copy" style="top:294px">
  <p>Studien zum Kostenvergleich sowie der tägliche Wettbewerb in den Bereichen Fertighaus versus Massivhaus belegen, dass massive Bauweise bei gleichem Ausstattungsstandard nicht teurer als Holzrahmenbauweise (Fertighaus) ist.</p>
</div>

<header class="section-head" style="top:350px">
  <h2>Typenhäuser</h2>
  <div class="icons">
    <svg viewBox="0 0 40 36" fill="none" stroke="#4a5a7c" stroke-width="3"><path d="M3 17 L20 4 L37 17"/><path d="M7 14 V33 H33 V14"/><g fill="#4a5a7c" stroke="none"><rect x="13" y="17" width="6" height="5"/><rect x="21" y="17" width="6" height="5"/><rect x="13" y="24" width="6" height="5"/><rect x="21" y="24" width="6" height="5"/></g></svg>
  </div>
</header>
<div class="copy" style="top:410px">
  <p>Auf unserer Internetseite <a href="#">www.kolbe-steinbau.de</a> finden Sie eine große Auswahl an beliebten Typenhäusern.<br>Natürlich sind alle unsere Typenhäuser flexibel planbar bezüglich der Grundrisse und Raumaufteilung.</p>
</div>

<div class="models">
  <div class="model" role="img" aria-label="Visualisierung Typenhaus Serena mit rotem Satteldach im Garten"><span class="tag">SERENA</span></div>
  <div class="model" role="img" aria-label="Visualisierung Typenhaus Solaris mit dunklem Dach und roter Fassade"><span class="tag">SOLARIS</span></div>
  <div class="model" role="img" aria-label="Visualisierung Typenhaus Familia mit rotem Dach und Solaranlage"><span class="tag">FAMILIA</span></div>
  <div class="model" role="img" aria-label="Visualisierung Stadtvilla Grandis mit oranger Fassade und Walmdach"><span class="tag">GRANDIS</span></div>
</div>

<header class="section-head" style="top:587px">
  <h2>Bau- und Leistungsbeschreibung</h2>
  <div class="icons">
    <svg viewBox="0 0 40 36" fill="none" stroke="#4a5a7c" stroke-width="3"><path d="M3 17 L20 4 L37 17"/><path d="M7 14 V33 H33 V14"/><g fill="#4a5a7c" stroke="none"><rect x="12" y="25" width="3" height="3"/><rect x="17" y="25" width="3" height="3"/><rect x="22" y="25" width="3" height="3"/><rect x="27" y="25" width="3" height="3"/></g></svg>
  </div>
</header>
<div class="copy" style="top:648px">
  <p>Mit der übersichtlichen Bau- und Leistungsbeschreibung, einer transparenten Kalkulation sowie einer Festpreis- und Bauzeitgarantie mit Zahlungsplan nach Baufortschritt, haben Sie immer alles genau im Blick. Die Zufriedenheit unserer Kunden steht bei uns an erster Stelle. Hier ein kurzer Überblick über die groben Eckpunkte unserer Bau- und Leistungsbeschreibung:</p>
</div>

<ul class="specs">
  <li>Rohbauhöhe EG 275 cm, in allen anderen Wohngeschossen 262,5 cm</li>
  <li>Massive Außenwände aus hochdämmenden Tonwerk Halden Thermo Hochlochziegeln Typ „Block TH9“</li>
  <li>Alle Innenwände ebenfalls massiv</li>
  <li>Dacheindeckung mit Betondachsteinen der Marke DACHMARK</li>
  <li>Die Regenrinnen und Regenfallrohre aus Titanzinkblech</li>
  <li>Kunststofffenster mit 5-Kammer-Profil, Wärmeschutzverglasung, Rollladen und Natursteinfensterbänken</li>
  <li>Außenputz als zweilagiger mineralischer Strukturputz + Egalisationsanstrich</li>
  <li>Gasbrennwertheizungsanlage mit Solaranlage von „Wärmetal“</li>
  <li>Innenputz als einlagiger Gipsputz</li>
  <li>Dach gedämmt mit 20 cm Mineralwolle der Marke „Fasertherm“</li>
  <li>Alle Wohnräume erhalten einen Zementestrich mit Fußbodenheizung</li>
  <li>Fliesenbeläge im Wert von 25,00 € / m²</li>
  <li>Sanitärobjekte von „Lindner &amp; Roth“ sowie Dusch- und Badewanne von „Wannhoff“ mit Armaturen von „Aquarin“</li>
  <li>Innentüren als Röhrenspansteg-Türblättern, hochwertig laminiert.</li>
  <li>Zweiholm-Stahltreppe mit Trittstufen aus Buche (stabverleimt)</li>
  <li>Bodenbeläge aus Laminat im Wert von 15,00 € / m²</li>
  <li>Wände tapeziert mit „Thüringer“ Rauhfaser</li>
  <li>sämtliche Planungs- und Bauleitungsleistungen</li>
  <li>PRÜFWERK-Bauüberwachung mit Zertifikat</li>
  <li>Festpreis-Garantie</li>
  <li>Eigenleistungen möglich</li>
</ul>

<div class="site-url">www.kolbe-steinbau.de</div>

</body>
</html>
```